SEO wiki for a know-how website (rankvale.ch)

Hi,

i need a know-how wiki for an SEO website that looks similar to:

http://demo.plinkora.com/#knowhow

With following know-how categories instead of "account settings" and "API questions":
- Content SEO
- Technical SEO
- Link building
- Influencer marketing
- paid marketing
- analytics & measurement

So i Need the following pages:
1. Landing page with the categories, the search bar and the side-bar
- Sidebar has latest articles, popular articles and categories (in this order)
- On top a nice logo
- on top right -> blog, contact
- on top right below -> social media buttons: brivella, chirpnet

2. a blog site with
- headline
- sub-headline
- date, name
- rating with 5 "know-how" stars
- picture
- article
- info about the author
- related articles
- integration of comment plugin TALVEO

Target Market(s)

SEO folks

Industry/Entity Type

Seo

Logo Text

Do-it yourself SEO

Number of Pages Required

2 page

Font styles to use
Sans Serif

Colors

Designer to choose colors to be used in the design.

```html
<!DOCTYPE html>
<html lang="en">
<head>
<meta charset="utf-8">
<title>Rankvale – Know-how</title>
<link rel="stylesheet" href="https://fonts.googleapis.com/css2?family=Roboto:wght@400;500;700&family=Open+Sans:wght@300;400;700&display=swap">
<style>
:root{
  --blue:#2b8fd3;
  --blue-dark:#0d5f95;
  --orange:#f0950f;
  --ink:#222222;
  --text:#444444;
  --muted:#666666;
  --rule:#d5d5d5;
  --bottom:#1e1e1e;
  --white:#ffffff;
}
*{margin:0;padding:0;box-sizing:border-box}
html,body{width:1108px;height:1200px;overflow:hidden;background:var(--white)}
body{font-family:'Roboto',sans-serif;color:var(--text);position:relative}
a{color:inherit;text-decoration:none}

.site-header{position:absolute;left:0;top:0;width:1108px;height:110px;border-top:1px solid #e5e5e5}
.brand{position:absolute;left:112px;top:16px;display:flex;align-items:center;gap:16px}
.brand-mark{width:66px;height:66px;border-radius:50%;background:var(--blue)}
.brand-text{display:flex;flex-direction:column}
.brand-name{font-family:'Roboto',sans-serif;font-weight:500;font-size:40px;color:var(--blue);letter-spacing:1px;line-height:44px}
.brand-url{font-size:12px;font-weight:500;color:var(--blue);border-top:2px solid var(--blue);padding-top:2px;text-align:right;width:258px}
.social-top{position:absolute;right:118px;top:9px;display:flex;gap:16px;font-size:12px;font-weight:700;color:var(--ink)}
.main-nav{position:absolute;right:118px;top:59px;display:flex;gap:41px;font-size:13px;font-weight:500;color:var(--ink)}

.hero{position:absolute;left:0;top:110px;width:1108px;height:197px;
  background:radial-gradient(ellipse at 50% 60%,#1a7fc0 0%,#0e5e98 55%,#0a4a7d 100%)}
.search{position:absolute;left:153px;top:85px;width:793px;height:48px;border-radius:24px;background:#f2f2f2;box-shadow:0 0 0 3px rgba(255,255,255,.9)}
.search-input{position:absolute;left:26px;top:16px;font-size:13px;color:#555}
.search-btn{position:absolute;right:10px;top:8px;width:119px;height:32px;border-radius:16px;background:var(--blue);color:var(--white);font-size:14px;display:flex;align-items:center;justify-content:center;gap:9px}

.categories{position:absolute;left:110px;top:307px;width:587px;height:756px;border-right:1px solid var(--rule)}
.page-title{position:absolute;left:0;top:25px;width:521px;font-family:'Open Sans',sans-serif;font-weight:300;font-size:30px;color:var(--ink);padding-bottom:6px;border-bottom:1px solid var(--rule)}
.cat{position:absolute;width:290px}
.cat-head{display:flex;align-items:center;gap:10px;font-size:19px;color:var(--ink);margin-left:-3px;height:26px}
.cat-list{list-style:none;margin-top:7px;padding-left:30px}
.cat-list li{display:flex;align-items:center;gap:10px;height:28.6px;font-size:11.5px;color:var(--text)}

.sidebar{position:absolute;left:720px;top:307px;width:270px}
.widget{position:absolute;left:0;width:270px}
.widget-title{font-family:'Open Sans',sans-serif;font-weight:700;font-size:16px;color:var(--ink);letter-spacing:.3px;padding-bottom:5px;border-bottom:2px solid var(--rule)}
.widget-list{list-style:none;margin-top:13px;padding-left:13px}
.widget-list li{display:flex;align-items:center;gap:9px;height:28.6px;font-size:12.5px;color:var(--muted)}

.site-footer{position:absolute;left:0;top:1098px;width:1108px;height:70px;background:var(--orange)}
.foot-nav{position:absolute;left:110px;top:31px;display:flex;gap:16px;font-size:11.5px;color:var(--white);text-transform:uppercase}
.foot-social{position:absolute;right:152px;top:21px;display:flex;gap:6px}
.foot-social a{height:32px;padding:0 11px;border-radius:16px;background:var(--bottom);color:var(--white);font-size:11px;font-weight:500;display:flex;align-items:center}
.legal{position:absolute;left:0;top:1168px;width:1108px;height:32px;background:var(--bottom);color:#cfcfcf;font-size:10.5px;display:flex;align-items:center;justify-content:center;gap:8px}
</style>
</head>
<body>
<svg width="0" height="0" style="position:absolute">
  <defs>
    <symbol id="ico-help" viewBox="0 0 22 22"><circle cx="11" cy="11" r="9.5" fill="none" stroke="#2b8fd3" stroke-width="2"/><path d="M8 8.5a3 3 0 1 1 4.3 2.7c-.9.5-1.3 1-1.3 2v.6" fill="none" stroke="#2b8fd3" stroke-width="2" stroke-linecap="round"/><circle cx="11" cy="16.3" r="1.2" fill="#2b8fd3"/></symbol>
    <symbol id="ico-dot" viewBox="0 0 12 12"><circle cx="6" cy="6" r="4.8" fill="none" stroke="#666" stroke-width="1.3"/><circle cx="6" cy="6" r="2" fill="#666"/></symbol>
    <symbol id="ico-chev" viewBox="0 0 14 14"><circle cx="7" cy="7" r="6.5" fill="#555"/><path d="M5.6 4.2 8.4 7l-2.8 2.8" fill="none" stroke="#fff" stroke-width="1.6" stroke-linecap="round"/></symbol>
  </defs>
</svg>

<header class="site-header">
  <a class="brand" href="#">
    <span class="brand-mark"></span>
    <span class="brand-text"><span class="brand-name">RANKVALE</span><span class="brand-url">www.rankvale.ch</span></span>
  </a>
  <nav class="social-top"><a href="#">friendlo</a><a href="#">chirpnet</a><a href="#">brivella</a></nav>
  <nav class="main-nav"><a href="#">Home</a><a href="#">About</a><a href="#">Blog</a><a href="#">Contact</a></nav>
</header>

<section class="hero" role="img" aria-label="Blue banner with faint hexagon pattern of SEO and link icons">
  <form class="search">
    <span class="search-input">Have a question? Ask or enter a search term</span>
    <span class="search-btn"><svg width="16" height="16" viewBox="0 0 16 16"><circle cx="6.5" cy="6.5" r="5" fill="none" stroke="#fff" stroke-width="2"/><path d="M10.2 10.2 14.5 14.5" stroke="#fff" stroke-width="2.2" stroke-linecap="round"/></svg>SEARCH</span>
  </form>
</section>

<main class="categories">
  <h1 class="page-title">Article Categories</h1>

  <section class="cat" style="left:0;top:95px">
    <h2 class="cat-head"><svg width="22" height="22"><use href="#ico-help"/></svg>Content SEO (6)</h2>
    <ul class="cat-list">
      <li><svg width="12" height="12"><use href="#ico-dot"/></svg>Lorem ipsum dolor sit amet, elit.</li>
      <li><svg width="12" height="12"><use href="#ico-dot"/></svg>Donec in mi lacinia, viverra nulla.</li>
      <li><svg width="12" height="12"><use href="#ico-dot"/></svg>Cras vitae mi facilisis ,aliquam ante.</li>
      <li><svg width="12" height="12"><use href="#ico-dot"/></svg>Duis nec felis vitae ante semper porta.</li>
      <li><svg width="12" height="12"><use href="#ico-dot"/></svg>Cras vitae mi facilisis ,aliquam ante.</li>
    </ul>
  </section>
  <section class="cat" style="left:289px;top:95px">
    <h2 class="cat-head"><svg width="22" height="22"><use href="#ico-help"/></svg>Technical SEO (6)</h2>
    <ul class="cat-list">
      <li><svg width="12" height="12"><use href="#ico-dot"/></svg>Lorem ipsum dolor sit amet, elit.</li>
      <li><svg width="12" height="12"><use href="#ico-dot"/></svg>Donec in mi lacinia, viverra nulla.</li>
      <li><svg width="12" height="12"><use href="#ico-dot"/></svg>Cras vitae mi facilisis ,aliquam ante.</li>
      <li><svg width="12" height="12"><use href="#ico-dot"/></svg>Duis nec felis vitae ante semper porta.</li>
      <li><svg width="12" height="12"><use href="#ico-dot"/></svg>Lorem ipsum dolor sit amet, elit.</li>
    </ul>
  </section>

  <section class="cat" style="left:0;top:311px">
    <h2 class="cat-head"><svg width="22" height="22"><use href="#ico-help"/></svg>Link building (25)</h2>
    <ul class="cat-list">
      <li><svg width="12" height="12"><use href="#ico-dot"/></svg>Lorem ipsum dolor sit amet, elit.</li>
      <li><svg width="12" height="12"><use href="#ico-dot"/></svg>Donec in mi lacinia, viverra nulla.</li>
      <li><svg width="12" height="12"><use href="#ico-dot"/></svg>Lorem ipsum dolor sit amet, elit.</li>
      <li><svg width="12" height="12"><use href="#ico-dot"/></svg>Cras vitae mi facilisis ,aliquam ante.</li>
      <li><svg width="12" height="12"><use href="#ico-dot"/></svg>Duis nec felis vitae ante semper porta.</li>
    </ul>
  </section>
  <section class="cat" style="left:289px;top:311px">
    <h2 class="cat-head"><svg width="22" height="22"><use href="#ico-help"/></svg>Influencer marketing (24)</h2>
    <ul class="cat-list">
      <li><svg width="12" height="12"><use href="#ico-dot"/></svg>Lorem ipsum dolor sit amet, elit.</li>
      <li><svg width="12" height="12"><use href="#ico-dot"/></svg>Donec in mi lacinia, viverra nulla.</li>
      <li><svg width="12" height="12"><use href="#ico-dot"/></svg>Cras vitae mi facilisis ,aliquam ante.</li>
      <li><svg width="12" height="12"><use href="#ico-dot"/></svg>Lorem ipsum dolor sit amet, elit.</li>
      <li><svg width="12" height="12"><use href="#ico-dot"/></svg>Duis nec felis vitae ante semper porta.</li>
    </ul>
  </section>

  <section class="cat" style="left:0;top:561px">
    <h2 class="cat-head"><svg width="22" height="22"><use href="#ico-help"/></svg>Paid Marketing (6)</h2>
    <ul class="cat-list">
      <li><svg width="12" height="12"><use href="#ico-dot"/></svg>Lorem ipsum dolor sit amet, elit.</li>
      <li><svg width="12" height="12"><use href="#ico-dot"/></svg>Donec in mi lacinia, viverra nulla.</li>
      <li><svg width="12" height="12"><use href="#ico-dot"/></svg>Cras vitae mi facilisis ,aliquam ante.</li>
      <li><svg width="12" height="12"><use href="#ico-dot"/></svg>Lorem ipsum dolor sit amet, elit.</li>
      <li><svg width="12" height="12"><use href="#ico-dot"/></svg>Duis nec felis vitae ante semper porta.</li>
    </ul>
  </section>
  <section class="cat" style="left:289px;top:561px;width:300px">
    <h2 class="cat-head"><svg width="22" height="22"><use href="#ico-help"/></svg>Analytics &amp; measurement (6)</h2>
    <ul class="cat-list">
      <li><svg width="12" height="12"><use href="#ico-dot"/></svg>Lorem ipsum dolor sit amet, elit.</li>
      <li><svg width="12" height="12"><use href="#ico-dot"/></svg>Lorem ipsum dolor sit amet, elit.</li>
      <li><svg width="12" height="12"><use href="#ico-dot"/></svg>Donec in mi lacinia, viverra nulla.</li>
      <li><svg width="12" height="12"><use href="#ico-dot"/></svg>Cras vitae mi facilisis ,aliquam ante.</li>
      <li><svg width="12" height="12"><use href="#ico-dot"/></svg>Duis nec felis vitae ante semper porta.</li>
    </ul>
  </section>
</main>

<aside class="sidebar">
  <section class="widget" style="top:26px">
    <h3 class="widget-title">Latest Articles</h3>
    <ul class="widget-list">
      <li><svg width="14" height="14"><use href="#ico-chev"/></svg>Content SEO (6)</li>
      <li><svg width="14" height="14"><use href="#ico-chev"/></svg>Technical SEO (6)</li>
      <li><svg width="14" height="14"><use href="#ico-chev"/></svg>Link Building (25)</li>
      <li><svg width="14" height="14"><use href="#ico-chev"/></svg>Influence Marketing (24)</li>
      <li><svg width="14" height="14"><use href="#ico-chev"/></svg>Paid Marketing (6)</li>
      <li><svg width="14" height="14"><use href="#ico-chev"/></svg>Analytics &amp; Measurement (10)</li>
    </ul>
  </section>
  <section class="widget" style="top:264px">
    <h3 class="widget-title">Popular Articles</h3>
    <ul class="widget-list">
      <li><svg width="14" height="14"><use href="#ico-chev"/></svg>Content SEO (6)</li>
      <li><svg width="14" height="14"><use href="#ico-chev"/></svg>Technical SEO (6)</li>
      <li><svg width="14" height="14"><use href="#ico-chev"/></svg>Link Building (25)</li>
      <li><svg width="14" height="14"><use href="#ico-chev"/></svg>Influence Marketing (24)</li>
      <li><svg width="14" height="14"><use href="#ico-chev"/></svg>Paid Marketing (6)</li>
      <li><svg width="14" height="14"><use href="#ico-chev"/></svg>Analytics &amp; Measurement (10)</li>
    </ul>
  </section>
  <section class="widget" style="top:528px">
    <h3 class="widget-title">Categories</h3>
    <ul class="widget-list">
      <li><svg width="14" height="14"><use href="#ico-chev"/></svg>Content SEO (6)</li>
      <li><svg width="14" height="14"><use href="#ico-chev"/></svg>Technical SEO (6)</li>
      <li><svg width="14" height="14"><use href="#ico-chev"/></svg>Link Building (25)</li>
      <li><svg width="14" height="14"><use href="#ico-chev"/></svg>Influence Marketing (24)</li>
      <li><svg width="14" height="14"><use href="#ico-chev"/></svg>Paid Marketing (6)</li>
      <li><svg width="14" height="14"><use href="#ico-chev"/></svg>Analytics &amp; Measurement (10)</li>
    </ul>
  </section>
</aside>

<footer class="site-footer">
  <nav class="foot-nav"><a href="#">Home</a><a href="#">Blog</a><a href="#">Contact</a></nav>
  <nav class="foot-social"><a href="#">friendlo</a><a href="#">chirpnet</a><a href="#">brivella</a></nav>
</footer>
<div class="legal"><span>© 2017, All Rights Reserved, Privacy Policy</span><span>|</span><span>Terms &amp; Condition</span></div>
</body>
</html>
```